Bramble Roofing Website Relaunch

We require a re-launch of our website, We are a longrun roofing company based in New Zealand, we are rapidly expanding and require a more professionally presented website our current website is www.brambleroofing.co.nz we want something modern, masculine and communicates a "strong" "superior" image, we already have a logo which I have attached we use the orange and silver one as you will see on our current website

Industry/Entity Type

It Company

Number of Pages Required

1 page

Colors
f37122
f78f20
000000
1b1b1b
474747
d3d3d3
f5f5f5

Requirements
Must have
• Images of our work
• Email and Mobile Contact Details
• Link to Chatterbox page
• Who We Are, What We Do
• Certified Trade Craftsman Logo
• Our Logo

```html
<!DOCTYPE html>
<html lang="en">
<head>
<meta charset="utf-8">
<title>Bramble Roofing – Long Run Roofing Specialists</title>
<link rel="stylesheet" href="https://fonts.googleapis.com/css2?family=Exo+2:wght@400;500;600;700&family=Open+Sans:wght@400;600;700&display=swap">
<style>
:root{
  --orange:#f37122;
  --orange-light:#f78f20;
  --black:#000000;
  --charcoal:#1b1b1b;
  --slate:#474747;
  --silver:#d3d3d3;
  --mist:#f5f5f5;
  --white:#ffffff;
  --text:#666666;
  --heading:#222222;
}
*{box-sizing:border-box;margin:0;padding:0}
html,body{width:1200px;height:2719px;overflow:hidden}
body{position:relative;background:var(--white);font-family:"Open Sans",Arial,sans-serif;color:var(--text)}
.abs{position:absolute}

/* hero */
.hero{position:absolute;left:0;top:0;width:1200px;height:433px;
  background:linear-gradient(180deg,#2a2c2e 0%,#3b3d3f 45%,#2b2a28 75%,#1f1d1b 100%)}
.hero-photo{position:absolute;inset:0;background:radial-gradient(ellipse at 50% 70%,rgba(120,110,95,.35),rgba(0,0,0,0) 60%)}
.brand{position:absolute;display:flex;align-items:center;gap:12px}
.brand-mark{width:34px;height:34px;background:var(--orange)}
.brand-name{font-family:"Exo 2",Arial,sans-serif;font-weight:700;color:var(--orange);letter-spacing:1px;line-height:1}
.hero-brand{left:470px;top:50px}
.hero-brand .brand-name{font-size:28px}
.main-nav{position:absolute;left:323px;top:132px;width:554px;height:28px;background:rgba(120,120,120,.55);
  display:flex;align-items:center;justify-content:space-around;font-family:"Exo 2",Arial,sans-serif;font-size:11px;font-weight:600;color:var(--white);letter-spacing:1px}
.main-nav a{color:var(--white);text-decoration:none;position:relative}
.main-nav a.active::after{content:"";position:absolute;left:50%;bottom:-9px;margin-left:-4px;border:4px solid transparent;border-bottom-color:var(--orange)}
.hero-title{position:absolute;left:0;width:1200px;top:224px;text-align:center;font-family:"Exo 2",Arial,sans-serif;font-weight:700;font-size:35px;color:var(--orange-light);letter-spacing:1.5px}
.hero-sub{position:absolute;left:0;width:1200px;top:273px;text-align:center;font-size:14px;font-weight:600;color:#e6e6e6}

/* section headings */
.section-head{position:absolute;left:172px;display:flex;align-items:center;width:856px}
.section-head::before{content:"";width:4px;height:20px;background:var(--orange);margin-right:30px}
.section-head h2{font-family:"Exo 2",Arial,sans-serif;font-weight:600;font-size:24px;color:var(--heading);white-space:nowrap}
.section-head h2 span{color:var(--orange)}
.section-head .rule{flex:1;height:14px;background:#dedede;margin-left:30px}
.intro{position:absolute;left:178px;width:850px;font-size:12px;line-height:24px;color:#777}

/* services */
.service{position:absolute;width:270px;height:189px;background:var(--mist)}
.service-photo{height:156px;border:1px solid #555}
.service-label{position:absolute;left:0;bottom:0;width:100%;height:33px;display:flex;align-items:center;justify-content:flex-end;padding-right:12px;font-family:"Exo 2",Arial,sans-serif;font-size:13px;font-weight:500;color:#222}
.service-tab{position:absolute;left:0;bottom:0;width:50px;height:33px}

/* about */
.about{position:absolute;left:0;top:1084px;width:1200px;height:417px;background:var(--slate)}
.about-head{position:absolute;left:537px;top:1148px;display:flex;align-items:center;width:491px}
.about-head::before{content:"";width:4px;height:20px;background:var(--orange);margin-right:30px}
.about-head h2{font-family:"Exo 2",Arial,sans-serif;font-weight:600;font-size:24px;color:var(--white)}
.about-head h2 span{color:var(--orange)}
.about-head .rule{flex:1;height:14px;background:#5a5a5a;margin-left:30px}
.about-copy{position:absolute;left:544px;top:1196px;width:486px;font-size:11px;line-height:20px;color:#e4e4e4}
.btn{position:absolute;display:flex;align-items:center;justify-content:center;background:var(--orange);color:var(--white);font-family:"Exo 2",Arial,sans-serif;font-size:15px;font-weight:500;box-shadow:3px 3px 0 #c85a17}
.badge{position:absolute;left:950px;top:1374px;width:76px;height:76px;background:var(--white);border:1px solid #999}
.badge-inner{position:absolute;left:12px;top:12px;width:52px;height:52px;border-radius:50%;background:#333}

/* works */
.works{position:absolute;left:0;top:1501px;width:1200px;height:865px;background:var(--mist)}
.filters{position:absolute;left:172px;top:1684px;width:856px;height:34px;background:var(--slate);display:flex;align-items:center;padding-left:18px;font-size:12px;color:#e0e0e0}
.filters span.sep{color:#999;margin:0 12px}
.filters .on{color:var(--orange);font-weight:700}
.gallery{position:absolute;left:167px;top:1737px;display:flex;gap:4px}
.gallery .col{width:214px;display:flex;flex-direction:column;gap:4px}
.shot{width:214px}

/* footer */
.footer{position:absolute;left:0;top:2366px;width:1200px;height:353px;background:var(--charcoal)}
.foot-title{position:absolute;top:2434px;font-family:"Exo 2",Arial,sans-serif;font-size:13px;font-weight:500;color:var(--orange)}
.footer-brand{left:180px;top:2490px}
.footer-brand .brand-mark{width:28px;height:28px}
.footer-brand .brand-name{font-size:22px}
.contact{position:absolute;left:180px;display:flex;align-items:center;gap:14px;font-size:11px;color:#8a8a8a}
.quick-links{position:absolute;left:479px;top:2476px;display:grid;grid-template-columns:83px 83px;gap:4px 7px}
.quick-links a{height:25px;display:flex;align-items:center;padding-left:14px;background:#232323;border:1px solid #2f2f2f;font-size:10.5px;color:#8a8a8a;text-decoration:none}
.quick-links a.wide{grid-column:span 2;width:113px}
.social{position:absolute;left:756px;top:2438px;width:272px;height:176px;background:var(--white)}
.social-cover{position:absolute;left:0;top:0;width:272px;height:100px;background:linear-gradient(180deg,#8a9096,#4d4a46)}
.social-name{position:absolute;left:50px;top:10px;font-size:11px;font-weight:700;color:var(--white)}
.social-likes{position:absolute;left:50px;top:25px;font-size:9px;color:#eee}
.social-avatar{position:absolute;left:10px;top:10px;width:34px;height:34px;background:var(--white);border:1px solid #ccc}
.social-btn{position:absolute;top:76px;height:16px;padding:0 6px;background:#f6f7f9;border:1px solid #ccd0d5;font-size:8.5px;font-weight:700;color:#4b4f56;display:flex;align-items:center}
.social-foot{position:absolute;left:6px;top:112px;font-size:8.5px;color:#666}
.social-friends{position:absolute;left:6px;top:128px;width:170px;height:24px;background:linear-gradient(90deg,#c9b29b,#9b8b7e,#b8a591)}
.foot-rule{position:absolute;left:178px;top:2643px;width:850px;height:1px;background:#2e2e2e}
.copyright{position:absolute;left:182px;top:2671px;font-size:10px;color:#6d6d6d}
.to-top{position:absolute;left:1072px;top:2682px}
</style>
</head>
<body>

<header class="hero">
  <div class="hero-photo" role="img" aria-label="Photograph of a house under construction with scaffolding and a new long run roof beneath a dark sky"></div>
  <div class="brand hero-brand">
    <span class="brand-mark"></span>
    <span class="brand-name">BRAMBLE ROOFING</span>
  </div>
  <nav class="main-nav">
    <a class="active" href="#">HOME</a>
    <a href="#">ABOUT</a>
    <a href="#">SERVICES</a>
    <a href="#">OUR WORK</a>
    <a href="#">CONTACT</a>
  </nav>
  <h1 class="hero-title">LONG RUN ROOFING SPECIALISTS</h1>
  <p class="hero-sub">Leaders in all long run colour steel, zinc-alloy installations &amp; roofing solutions</p>
</header>

<!-- services -->
<div class="section-head" style="top:488px"><h2>Our <span>Quality Services</span></h2><div class="rule"></div></div>
<p class="intro" style="top:533px">At Bramble Roofing we offer a variety of professional services specializing in Residential, Industrial and Commercial Long Run Roofing Installations. We offer a no obligation free quotation, inspection and consultation service.&nbsp;&nbsp; Providing un-biased, honest advice whilst determining services required.</p>

<div class="service" style="left:172px;top:616px">
  <div class="service-photo" role="img" aria-label="Photo of a weatherboard house with a new roof" style="background:linear-gradient(180deg,#8fb4d8,#c9d3dc 50%,#6f8a4f)"></div>
  <div class="service-label">New Roofs and Re-roofs</div>
  <svg class="service-tab" viewBox="0 0 50 33"><polygon points="0,0 38,0 50,16.5 38,33 0,33" fill="#f37122"/><path d="M12 18 L22 10 L32 18 M15 16 V24 H29 V16" fill="none" stroke="#fff" stroke-width="2"/></svg>
</div>
<div class="service" style="left:466px;top:616px">
  <div class="service-photo" role="img" aria-label="Photo of a shed clad in green metal cladding" style="background:linear-gradient(180deg,#d8dde0,#4f5f45 55%,#7a7566)"></div>
  <div class="service-label">Metal Cladding</div>
  <svg class="service-tab" viewBox="0 0 50 33"><polygon points="0,0 38,0 50,16.5 38,33 0,33" fill="#f37122"/><path d="M11 21 L15 14 L19 21 L23 14 L27 21 L31 14" fill="none" stroke="#fff" stroke-width="2"/></svg>
</div>
<div class="service" style="left:758px;top:616px">
  <div class="service-photo" role="img" aria-label="Photo of a black clad building with new spouting and fascia" style="background:linear-gradient(180deg,#b7c4cc,#2b2e30 40%,#2a2c2c 80%,#6e7a4a)"></div>
  <div class="service-label">Spouting and Metal Fascia</div>
  <svg class="service-tab" viewBox="0 0 50 33"><polygon points="0,0 38,0 50,16.5 38,33 0,33" fill="#f37122"/><path d="M11 11 H31 V15 H24 V25 H20 V15 H11 Z" fill="#fff"/></svg>
</div>
<div class="service" style="left:172px;top:845px">
  <div class="service-photo" role="img" aria-label="Photo of vertical metal cladding and a downpipe" style="background:linear-gradient(90deg,#4a4a4a,#8a8a8a 50%,#3a3a3a)"></div>
  <div class="service-label">Down Pipes</div>
  <svg class="service-tab" viewBox="0 0 50 33"><polygon points="0,0 38,0 50,16.5 38,33 0,33" fill="#f37122"/><path d="M14 10 C12 12 13 18 18 23 C23 27 27 26 29 24 L26 21 L23 23 C21 22 17 18 16 16 L18 13 Z" fill="#fff"/></svg>
</div>
<div class="service" style="left:466px;top:845px">
  <div class="service-photo" role="img" aria-label="Photo of a dark roof alteration viewed from above" style="background:linear-gradient(180deg,#a9c2d9,#6f8a4f 35%,#2a3340 70%,#3c4650)"></div>
  <div class="service-label">Alterations</div>
  <svg class="service-tab" viewBox="0 0 50 33"><polygon points="0,0 38,0 50,16.5 38,33 0,33" fill="#f37122"/><path d="M14 10 H28 V25 H14 Z M17 14 H25 M17 18 H25 M17 22 H25" fill="none" stroke="#fff" stroke-width="2"/></svg>
</div>
<div class="service" style="left:758px;top:845px">
  <div class="service-photo" role="img" aria-label="Photo of a house extension with scaffolding and a grey roof" style="background:linear-gradient(180deg,#c5d3dd,#9aa0a3 40%,#8c7f6c 75%,#6d7550)"></div>
  <div class="service-label">Extensions</div>
  <svg class="service-tab" viewBox="0 0 50 33"><polygon points="0,0 38,0 50,16.5 38,33 0,33" fill="#f37122"/><path d="M11 24 L17 15 L22 21 L25 17 L31 24 Z M26 12 A2 2 0 1 0 26.1 12" fill="#fff"/></svg>
</div>

<!-- about -->
<section class="about">
  <svg class="abs" style="left:0;top:0" width="520" height="417" viewBox="0 0 520 417">
    <polygon points="0,0 390,0 512,208 390,417 0,417" fill="#f37122"/>
  </svg>
  <div class="abs" role="img" aria-label="Photograph of a large new roof installation across a commercial building"
       style="left:0;top:0;width:508px;height:417px;clip-path:polygon(0 0,383px 0,505px 208px,383px 417px,0 417px);background:linear-gradient(180deg,#6f9fd0 0%,#a8c6e2 28%,#6a7a58 36%,#4a5158 55%,#2a2f36 100%)"></div>
</section>
<div class="about-head"><h2>About <span>Us</span></h2><div class="rule"></div></div>
<p class="about-copy">We are a local, family owned and operated company with over 18 years extensive experience in the roofing industry, Roofing not only Waikato and Auckland but surrounding areas also. We are committed to providing superior service to our customers regardless of how big or small your project is, Your satisfaction is our guarantee. We take pride in installing quality products, Offering a workmanship guarantee and manufacturers material warranties where applicable. In a fast paced advancing industry we are constantly striving to provide the latest, modern quality installation methods available to ensure customer expectations are exceeded, project targets are met and a high quality finished product is delivered every time.</p>
<a class="btn" style="left:538px;top:1398px;width:134px;height:30px">Get A Quote</a>
<div class="badge" role="img" aria-label="Certified Trade Craftsman badge"><div class="badge-inner"></div></div>

<!-- recent works -->
<section class="works"></section>
<div class="section-head" style="top:1567px"><h2>Our <span>Recent Works</span></h2><div class="rule"></div></div>
<p class="intro" style="top:1614px">Liaising with our customers throughout the entire process from planning and design through to installation and signing off the completed project. Head on over to our Chatterbox page @brambleroofingltdnz for regular Project Updates, Client Comments and References.</p>
<div class="filters">
  <span class="on">All</span><span class="sep">/</span>
  <span>New Roofs and Re-roofs</span><span class="sep">/</span>
  <span>Metal Cladding</span><span class="sep">/</span>
  <span>Spouting and Metal Fascia</span><span class="sep">/</span>
  <span>Down Pipes</span><span class="sep">/</span>
  <span>Alterations</span><span class="sep">/</span>
  <span>Extensions</span>
</div>
<div class="gallery">
  <div class="col">
    <div class="shot" style="height:216px;background:linear-gradient(180deg,#7aa6d6,#3c4450 45%,#22262b)" role="img" aria-label="Photo of a dark long run roof close up"></div>
    <div class="shot" style="height:158px;background:linear-gradient(180deg,#6c9bd0,#a6bfd6 35%,#2e343b 70%,#50565c)" role="img" aria-label="Photo of roof sheets on a commercial building"></div>
    <div class="shot" style="height:136px;background:linear-gradient(180deg,#6f9fd6,#8a9aa8 55%,#7b7d74)" role="img" aria-label="Photo of a steel frame structure ready for roofing"></div>
  </div>
  <div class="col">
    <div class="shot" style="height:285px;background:linear-gradient(180deg,#7a8aa0,#c7a77c 30%,#24262a 55%,#141414)" role="img" aria-label="Photo of an open shed at dusk"></div>
    <div class="shot" style="height:163px;background:linear-gradient(180deg,#c9d3da,#9b968c 55%,#4f6a3a)" role="img" aria-label="Photo of a new house with scaffolding"></div>
  </div>
  <div class="col">
    <div class="shot" style="height:158px;background:linear-gradient(180deg,#dfe4e6,#c4c7c6 55%,#7f9a5a)" role="img" aria-label="Photo of a house with a new grey roof"></div>
    <div class="shot" style="height:283px;background:linear-gradient(180deg,#b6c5d0,#9aa0a2 35%,#7e6a52 65%,#6b6a44)" role="img" aria-label="Photo of a roofing site on a hillside"></div>
  </div>
  <div class="col">
    <div class="shot" style="height:136px;background:linear-gradient(180deg,#5f97d2,#3b3735 55%,#5a8a35)" role="img" aria-label="Photo of a dark roofed home on a lawn"></div>
    <div class="shot" style="height:103px;background:linear-gradient(180deg,#c8d2d6,#2a2d30 45%,#5f6b44)" role="img" aria-label="Photo of black cladding on a shed"></div>
    <div class="shot" style="height:105px;background:linear-gradient(90deg,#d9dfe2,#2b2e31 45%,#2b2e31)" role="img" aria-label="Photo of black clad building with a window"></div>
    <div class="shot" style="height:136px;background:linear-gradient(180deg,#6f9ad0,#c8d2da 45%,#5a5a52 70%,#7a8b5a)" role="img" aria-label="Photo of a new roof on a suburban house"></div>
  </div>
</div>
<a class="btn" style="left:533px;top:2279px;width:134px;height:32px">View All</a>

<!-- footer -->
<footer class="footer"></footer>
<div class="foot-title" style="left:178px">ABOUT US</div>
<div class="foot-title" style="left:479px">QUICK LINKS</div>
<div class="brand footer-brand">
  <span class="brand-mark"></span>
  <span class="brand-name">BRAMBLE ROOFING</span>
</div>
<div class="contact" style="top:2553px">
  <svg width="10" height="10" viewBox="0 0 10 10"><path d="M2 0 C0 1 0 4 3 7 C6 10 9 10 10 8 L8 6 L6.5 7 C5 6.5 3.5 5 3 3.5 L4 2 Z" fill="#8a8a8a"/></svg>
  <span>hello@brambleroofing.co.nz</span>
</div>
<div class="contact" style="top:2580px">
  <svg width="10" height="8" viewBox="0 0 10 8"><rect width="10" height="8" fill="#8a8a8a"/><path d="M0 0 L5 4 L10 0" fill="none" stroke="#1b1b1b" stroke-width="1"/></svg>
  <span>021 555 01234</span>
</div>
<nav class="quick-links">
  <a href="#">about</a><a href="#">services</a>
  <a href="#">gallery</a><a href="#">recent works</a>
  <a class="wide" href="#">Terms &amp; conditions</a>
  <a class="wide" href="#">Privacy Policy</a>
</nav>
<div class="social">
  <div class="social-cover" role="img" aria-label="Cover photo of a roofed building on the Bramble Roofing social page"></div>
  <div class="social-avatar"></div>
  <div class="social-name">Bramble Roofing</div>
  <div class="social-likes">25,076 Likes</div>
  <div class="social-btn" style="left:8px">Like Page</div>
  <div class="social-btn" style="left:214px">Share</div>
  <div class="social-foot">Be the first of your friends to like this</div>
  <div class="social-friends" role="img" aria-label="Row of follower profile pictures"></div>
</div>
<div class="foot-rule"></div>
<p class="copyright">Copyright © 2017 Bramble Roofing Ltd</p>
<svg class="to-top" width="16" height="14" viewBox="0 0 16 14"><path d="M2 7 L8 1 L14 7 M2 13 L8 7 L14 13" fill="none" stroke="#f37122" stroke-width="2"/></svg>

</body>
</html>
```